TK Fiscal Website Redesign Contest

We want to refresh our website to be more insitutional, professional for an international audience. We have designed a new logo for this purpose and that has been attached. A full brand brief and positioning statement has also been attached. Please read through all the documents carefully before designing. The old website is found here: https://tk-fiscal-example.com/

Target Market(s)

Actuaries and associated businesses internationally

Industry/Entity Type

professional services - actuaries

Number of Pages Required

3 page

Font styles to use
Sans Serif

Colors
0054AA
0677BA
7BADD7
CADEEF
E8F1F8
0094D4
00A9DD
6FCCEA
C7EBF8
E9F6FB
F0912C
F2A743
F7CA91
FBE8D2
FDF5EE
EE7325
F08F49
F5BC92
FAE3D3
FDF4ED
EB3D1F
EC4F4E
F09395
F8D3D4
FCEDEE

Requirements
Must have
• blues and greens to match the logo color, complimentary colors, navigation
Nice to have
• old site: https://tk-fiscal-example.com/

```html
<!DOCTYPE html>
<html lang="en">
<head>
<meta charset="utf-8">
<title>TK Fiscal — Request a Technical Walkthrough</title>
<link href="https://fonts.googleapis.com/css2?family=Inter:wght@400;500;600;700&display=swap" rel="stylesheet">
<style>
  :root {
    --navy: #0d1a2b;
    --blue: #0054aa;
    --header-bg: #f3f3f3;
    --ink: #1b2430;
    --nav-ink: #2a3440;
    --field-border: #dfe3e8;
    --hero-sub: #c9d1dc;
    --footer-text: #aab3bf;
    --footer-rule: #27334a;
    --white: #ffffff;
  }
  * { box-sizing: border-box; margin: 0; padding: 0; }
  html, body { width: 1200px; height: 1016px; overflow: hidden; }
  body { font-family: "Inter", sans-serif; background: var(--white); color: var(--ink); position: relative; }

  .site-header { position: absolute; top: 0; left: 0; width: 1200px; height: 63px; background: var(--header-bg); }
  .brand-name { position: absolute; left: 189px; top: 19px; font-size: 19px; font-weight: 600; color: var(--ink); letter-spacing: 0.5px; }
  .main-nav a { position: absolute; top: 24px; font-size: 11px; color: var(--nav-ink); text-decoration: none; }
  .main-nav a.current { color: #1f4d3f; }
  .btn { display: flex; align-items: center; justify-content: center; background: var(--blue); color: var(--white); font-size: 11px; font-weight: 500; border-radius: 2px; text-decoration: none; border: 0; font-family: inherit; }
  .header-cta { position: absolute; left: 817px; top: 17px; width: 196px; height: 29px; }

  .hero { position: absolute; top: 63px; left: 0; width: 1200px; height: 236px; background: var(--navy); text-align: center; }
  .hero h1 { position: absolute; top: 37px; left: 0; width: 1200px; font-size: 34px; font-weight: 600; color: var(--white); letter-spacing: -0.6px; }
  .hero p { position: absolute; top: 97px; left: 395px; width: 410px; font-size: 17.3px; line-height: 27.6px; color: var(--hero-sub); }

  .request-form label { position: absolute; font-size: 10.5px; font-weight: 500; color: var(--ink); }
  .field { position: absolute; border: 1px solid var(--field-border); background: var(--white); }
  .submit { position: absolute; left: 402px; top: 684px; width: 107px; height: 28px; }

  .site-footer { position: absolute; top: 770px; left: 0; width: 1200px; height: 246px; background: var(--navy); color: var(--footer-text); }
  .footer-brand { position: absolute; left: 187px; top: 46px; font-size: 17.5px; font-weight: 600; color: var(--white); }
  .footer-tagline { position: absolute; left: 187px; top: 83px; width: 220px; font-size: 13px; line-height: 21px; }
  .footer-col h4 { position: absolute; top: 46px; font-size: 10px; font-weight: 600; color: var(--white); letter-spacing: 0.3px; }
  .footer-col a, .legal a, .copyright { position: absolute; font-size: 10.3px; color: var(--footer-text); text-decoration: none; }
  .footer-rule { position: absolute; left: 187px; top: 183px; width: 826px; height: 1px; background: var(--footer-rule); }
</style>
</head>
<body>
  <header class="site-header">
    <div class="brand-name">TK Fiscal</div>
    <nav class="main-nav">
      <a href="#" style="left:406px">Home</a>
      <a href="#" style="left:457px">Platform</a>
      <a href="#" style="left:521px">Solutions</a>
      <a href="#" style="left:588px">Insights</a>
      <a href="#" style="left:649px">Company</a>
      <a href="#" class="current" style="left:718px">Contact</a>
    </nav>
    <a href="#" class="btn header-cta">Request a Technical Walkthrough</a>
  </header>

  <section class="hero">
    <h1>Request a Technical Walkthrough</h1>
    <p>Connect with our engineering team for a detailed review of the platform's architectural and methodological capabilities.</p>
  </section>

  <form class="request-form">
    <label style="left:402px;top:358px">First Name</label>
    <div class="field" style="left:402px;top:378px;width:189px;height:30px"></div>
    <label style="left:609px;top:358px">Last Name</label>
    <div class="field" style="left:609px;top:378px;width:189px;height:30px"></div>
    <label style="left:402px;top:427px">Professional Email</label>
    <div class="field" style="left:402px;top:447px;width:396px;height:30px"></div>
    <label style="left:402px;top:496px">Organization</label>
    <div class="field" style="left:402px;top:516px;width:396px;height:30px"></div>
    <label style="left:402px;top:565px">Area of Interest (Optional)</label>
    <div class="field" style="left:402px;top:585px;width:396px;height:65px"></div>
    <button type="button" class="btn submit">Submit Request</button>
  </form>

  <footer class="site-footer">
    <div class="footer-brand">TK Fiscal</div>
    <p class="footer-tagline">Actuarial software for structured, auditable financial analysis.</p>
    <div class="footer-col">
      <h4 style="left:600px">NAVIGATION</h4>
      <a href="#" style="left:600px;top:74px">Platform</a>
      <a href="#" style="left:600px;top:103px">Solutions</a>
      <a href="#" style="left:600px;top:132px">Insights</a>
    </div>
    <div class="footer-col">
      <h4 style="left:824px">COMPANY</h4>
      <a href="#" style="left:824px;top:74px">About Us</a>
      <a href="#" style="left:824px;top:103px">Contact</a>
      <a href="#" style="left:824px;top:132px">Careers</a>
    </div>
    <div class="footer-rule"></div>
    <span class="copyright" style="left:187px;top:208px">© 2026 TK Fiscal. All rights reserved.</span>
    <div class="legal">
      <a href="#" style="left:848px;top:208px">Privacy Policy</a>
      <a href="#" style="right:187px;top:208px">Terms of Service</a>
    </div>
  </footer>
</body>
</html>
```